Design Creative Banner or Gif Ads. 3 Designs To Be Selected

Come up with some creative banner ads for crestline.co.nz

*At least 3 different winning banners will be chosen*

Please provide banner ads / gif ads in common google ads / website banner formats.

They can be gif or static but must stand out while still maintaining clear clean text and visuals, with a premium professional feel (please avoid clip art or anything that gives a cheap message).

Please keep in mind that these will likely be small ads so text needs to be large and if there's there a lot of text then use multiple frames/ pages as submit as a gif.

Style
Minimal & clean lines
Architectural or realistic images
Avoid cartoon styles, clipart, or anything that looks cheap

Font
Nexa or Montserrat or similar

Tone
Premium, serious, trustworthy — fits new builds

Colours
Option 1: Deep Navy (trust & quality) & lighter blues and warm grey
Option 2: Open to bright colours to help the ads stand out, such as (but not limited to) bright pink with black, yellow, fluorescent green, provided the messaging is still done professionally.
Our logo is attached (Crest Line Logo)

Display Sizes
Ad specs for file sizes should be file formats like JPEG, GIF, and PNG, with animations limited to a max of 30 seconds or less.
We will need several different ad sizes provided for each of the 3 selected winning designs.

• Medium Rectangle: 300 × 250 pixels
• Leaderboard: 728 × 90 pixels
• Desktop Banner ad image: (640x360 pixels)
• Desktop Banner ad image 2: (300x600 pixels)
• Possibly one or two other sizes

Flexibility to be creative
The ad text, words, upper/lower case, layout, colour, theme, and images can be adjusted to how you think it will look best. The follow example ads are just examples of what we are after but we are keen to see what you can create.

Recommendations at this point:
1. Avoid text heavy
2. Looking for more Gif ads
3. Imaging: if possible use real stock photo's rather than AI

Themes:

1
Building Soon? Start Here
Free Build Planning Pack:
✓ Build Cost Calculator
✓ Hidden Cost Checklist
✓ Builder Comparison Guide
Build With Confidence
Download Free

2
Before You Choose A Builder
Compare Price, Scope, Risk & Value
Avoid Costly Mistakes
Choose The Right Builder With Confidence
Download The Free Guide

3
Planning A New Build?
Avoid These Common Mistakes:
✗ Hidden Exclusions
✗ Missing Scope
✗ Unrealistic Allowances
✗ Budget Blowouts
Download The Free Guide

4
Before You Buy Land
Know what it could cost to build.
Avoid Costly Building Mistakes
Download Our Free Guides

5
Know Your Build Budget?
• Free Build Cost Calculator
• Hidden Cost Checklist
• Build Planning Tools
Calculate Costs (Download)

Target Market(s)

Landowners looking to build

Industry/Entity Type

Building

Font styles to use
Other font styles liked:
• Nexa or Montserrat or similar

Requirements
Should not have
• Avoid cartoon styles, clipart, or anything that looks cheap

```html
<!DOCTYPE html>
<html lang="en">
<head>
<meta charset="utf-8">
<title>Crest Line – Planning a New Build?</title>
<link rel="stylesheet" href="https://fonts.googleapis.com/css2?family=Montserrat:wght@500;600;700;800&display=swap">
<style>
  :root {
    --navy-deep: #0b2547;
    --navy: #12386a;
    --blue-mid: #1d5a9c;
    --blue-light: #5fb2e6;
    --sky: #8fd0f4;
    --white: #ffffff;
    --brand-navy: #163a63;
    --orange: #f47a1f;
    --orange-dark: #e0630e;
    --photo-warm: #b89a7c;
    --photo-cool: #8aa3bd;
  }
  * { margin: 0; padding: 0; box-sizing: border-box; }
  html, body {
    width: 1200px;
    height: 148px;
    overflow: hidden;
    background: var(--white);
  }
  .leaderboard {
    position: relative;
    width: 1200px;
    height: 148px;
    overflow: hidden;
    font-family: "Montserrat", sans-serif;
    background: linear-gradient(90deg, var(--navy-deep) 30%, var(--navy) 70%);
  }
  .build-photo {
    position: absolute;
    top: 0;
    right: 0;
    width: 440px;
    height: 148px;
    background:
      linear-gradient(90deg, var(--navy) 0%, rgba(18,56,106,0.55) 22%, rgba(18,56,106,0) 45%),
      linear-gradient(160deg, var(--photo-cool) 0%, #d6dde4 35%, var(--photo-warm) 70%, #5d4a3a 100%);
  }
  .chevron-panel {
    position: absolute;
    top: 0;
    left: 0;
    width: 420px;
    height: 148px;
  }
  .brand {
    position: absolute;
    left: 44px;
    top: 50px;
    display: flex;
    flex-direction: column;
    gap: 6px;
  }
  .brand-row {
    display: flex;
    align-items: center;
    gap: 12px;
  }
  .brand-square {
    width: 22px;
    height: 22px;
    background: var(--brand-navy);
  }
  .brand-name {
    font-size: 32px;
    font-weight: 600;
    color: var(--brand-navy);
    letter-spacing: -0.3px;
    line-height: 1;
  }
  .brand-tagline {
    font-size: 9.5px;
    font-weight: 600;
    color: var(--blue-mid);
    letter-spacing: 0.2px;
    text-transform: uppercase;
  }
  .offer {
    position: absolute;
    left: 424px;
    top: 16px;
  }
  .headline {
    font-size: 31px;
    font-weight: 800;
    color: var(--white);
    line-height: 1.1;
    letter-spacing: 0.3px;
  }
  .subline {
    margin-top: 6px;
    font-size: 20px;
    font-weight: 700;
    color: var(--sky);
    letter-spacing: 0.4px;
  }
  .cta {
    display: inline-block;
    margin-top: 12px;
    padding: 10px 26px;
    border-radius: 24px;
    background: linear-gradient(180deg, var(--orange) 0%, var(--orange-dark) 100%);
    color: var(--white);
    font-size: 16px;
    font-weight: 700;
    letter-spacing: 0.3px;
    text-transform: uppercase;
  }
</style>
</head>
<body>
  <div class="leaderboard">
    <div class="build-photo" role="img" aria-label="Photo of a model house, a hard hat and a hand with a pencil over building plans beside a calculator"></div>

    <svg class="chevron-panel" viewBox="0 0 420 148" aria-hidden="true">
      <polygon points="0,0 350,0 398,74 350,148 0,148" fill="var(--blue-light)"/>
      <polygon points="0,0 338,0 384,74 338,148 0,148" fill="var(--blue-mid)"/>
      <polygon points="0,0 318,0 364,74 318,148 0,148" fill="var(--navy-deep)"/>
      <polygon points="0,0 306,0 352,74 306,148 0,148" fill="var(--white)"/>
    </svg>

    <div class="brand">
      <div class="brand-row">
        <span class="brand-square"></span>
        <span class="brand-name">Crest Line</span>
      </div>
      <span class="brand-tagline">Compare quotes from trusted builders</span>
    </div>

    <div class="offer">
      <h1 class="headline">PLANNING A NEW BUILD?</h1>
      <p class="subline">CALCULATE YOUR BUILD COST</p>
      <span class="cta">Free Build Cost Calculator</span>
    </div>
  </div>
</body>
</html>
```